New College Graduate Resume - Creative and unique design that stands out from the rest

Need creative resume design for recent college graduate who graduated from School of Music with a concentration in music composition and production. Striving for a contemporary layout/design that allows the resume to "be unique" and "stand out" but be polished and professional. Open to integrating moderate color/graphics as part of resume design but the design can be minus those attributes as well. Attached is raw content in 7 sections (name/contact info, education, highlights of qualifications, work experience, honors/awards, and professional affiliations). While the designer has full latitude over overall design which (section headers, font type, separation/spacing, use of bullets, justification of text, etc.) please maintain current order/sequence of the 7 sections.

Industry/Entity Type

School

Requirements
Must have
• Name (Tobias Hale Whitcombe II) should be most prominent (bold/font size) compared to remainder of resume copy.
• Section headers should be prominent but less so when compared to name on resume.
• The attached file of resume content is provided as raw source copy and is NOT to be just copied and pasted into open fields as is. Expectation is each section of copy will be organized in a manner that is most visually appealing and may include bullets, appropriate spacing, etc.
Should not have
• The attached file of resume content is provided as source copy and is NOT to be just copied and pasted into open fields as is. Expectation is each section of copy will be organized in a manner that

```html
<!DOCTYPE html>
<html lang="en">
<head>
<meta charset="utf-8">
<title>Tobias Hale Whitcombe II – Resume</title>
<link href="https://fonts.googleapis.com/css2?family=Source+Sans+3:wght@400;500&display=swap" rel="stylesheet">
<style>
:root{
  --teal:#82cbd3;
  --teal-deep:#4fa9b3;
  --teal-soft:#b4dee2;
  --charcoal:#58585a;
  --ink:#4d4d4f;
  --grey-col:#e6e6e6;
  --white:#ffffff;
}
*{margin:0;padding:0;box-sizing:border-box}
html,body{width:841px;height:1200px;overflow:hidden;background:var(--white)}
body{font-family:"Source Sans 3",sans-serif;color:var(--ink);position:relative}
.header{position:absolute;left:0;top:0;width:841px;height:165px;background:var(--teal)}
.monogram{position:absolute;left:54px;top:20px;width:128px;height:128px;border-radius:50%;background:var(--teal-soft);box-shadow:4px 4px 10px rgba(0,0,0,.18);z-index:2;display:flex;align-items:center;justify-content:center;color:var(--white);font-size:58px;letter-spacing:2px}
.monogram .bar{display:inline-block;width:2px;height:64px;background:var(--white);margin:0 10px}
.name-pill{position:absolute;left:161px;top:54px;width:568px;height:68px;background:var(--white);border-radius:0 34px 34px 0;display:flex;justify-content:center;align-items:center;padding-left:40px}
.name{font-size:35px;font-weight:400;color:var(--ink);letter-spacing:.2px}
.tagline{position:absolute;left:308px;top:114px;width:272px;height:29px;background:var(--charcoal);color:var(--white);font-size:19px;display:flex;align-items:center;justify-content:center;z-index:3}
.contact-band{position:absolute;left:0;top:165px;width:841px;height:42px;background:var(--charcoal);display:flex;align-items:center;padding-left:35px;color:var(--teal);font-size:16px;gap:10px}
.contact-band svg{flex:none}
.contact-band .dot{margin:0 10px}
.side{position:absolute;left:518px;top:207px;width:323px;height:993px;background:var(--grey-col)}
.bar-head{position:absolute;left:0;height:32px;background:var(--teal);color:var(--white);font-size:16px;border-radius:0 16px 16px 0;display:flex;align-items:center;justify-content:center}
.education-head{top:231px;width:338px}
.work-head{top:478px;width:398px}
.education{position:absolute;left:18px;top:276px;width:480px;font-size:16px;line-height:20px;list-style:none}
.education li{position:relative;padding-left:20px;margin-bottom:8px}
.education li::before{content:"";position:absolute;left:3px;top:7px;width:6px;height:6px;border-radius:50%;background:var(--ink)}
.job{position:absolute;left:18px;width:490px}
.job::before{content:"";position:absolute;left:3px;top:7px;width:6px;height:6px;border-radius:50%;background:var(--ink)}
.job .dates{position:absolute;left:17px;top:0;font-size:16px;line-height:20px}
.job .rule{position:absolute;left:172px;top:0;width:1px;background:#cfcfcf}
.job .org{margin-left:190px;font-size:16px;line-height:20px}
.job .org span{display:block;padding-left:5px}
.job .role{margin-left:194px;margin-top:6px;font-size:12px;line-height:15.3px;width:296px}
.side-head{position:absolute;left:547px;width:248px;height:33px;border:1.5px solid var(--teal-deep);color:var(--teal-deep);font-size:16px;display:flex;align-items:center;justify-content:center;background:transparent}
.profile{position:absolute;left:548px;top:275px;width:280px;font-size:13.6px;line-height:16.9px}
.profile p+p{margin-top:4px}
.quals{position:absolute;left:548px;top:552px;list-style:none;font-size:12.5px;text-transform:uppercase;line-height:21.7px}
.honors,.affils{position:absolute;left:547px;width:290px;list-style:none;font-size:12.3px;line-height:15.5px}
.honors{top:883px}
.honors li{margin-bottom:7px}
.affils{top:1057px}
.affils li{margin-bottom:7px}
</style>
</head>
<body>
<header class="header">
  <div class="monogram">C<span class="bar"></span>V</div>
  <div class="name-pill"><h1 class="name">Tobias Hale Whitcombe II</h1></div>
  <div class="tagline">• COLLEGE GRADUATE •</div>
</header>

<div class="contact-band">
  <svg width="28" height="18" viewBox="0 0 28 18"><rect x="1" y="1" width="26" height="16" fill="none" stroke="#82cbd3" stroke-width="2"/><path d="M1 1 L14 11 L27 1 M1 17 L11 9 M27 17 L17 9" fill="none" stroke="#82cbd3" stroke-width="2"/></svg>
  <span>thwhitcombe@mailbox.net</span><span class="dot">•</span>
  <svg width="16" height="26" viewBox="0 0 16 26"><rect x="1" y="1" width="14" height="24" rx="2" fill="none" stroke="#82cbd3" stroke-width="2"/><rect x="3" y="4" width="10" height="15" fill="#82cbd3"/><circle cx="8" cy="22" r="1.3" fill="#82cbd3"/></svg>
  <span>404-555-0186</span><span class="dot">•</span>
  <svg width="18" height="24" viewBox="0 0 18 24"><path d="M9 0 C4 0 0 4 0 9 C0 15 9 24 9 24 C9 24 18 15 18 9 C18 4 14 0 9 0Z" fill="#82cbd3"/><circle cx="9" cy="9" r="3.5" fill="#58585a"/></svg>
  <span>218 Larkspur Lane - Atlanta, Georgia&nbsp; 30311</span>
</div>

<aside class="side"></aside>

<h2 class="bar-head education-head">EDUCATION</h2>
<ul class="education">
  <li>"Coral Bay University – Linden School of Music"<br>Coral Springs, Florida</li>
  <li>Bachelor of Music – May 2016<br>Major: Media Writing and Production,<br>GPA 3.20/4.0</li>
  <li>Briarwood Academy<br>College Park, Georgia<br>High School Diploma with Honors – May 2011</li>
</ul>

<h2 class="bar-head work-head">WORK EXPERIENCE</h2>
<article class="job" style="top:523px">
  <div class="dates">05. 2014 – Present</div>
  <div class="rule" style="height:226px"></div>
  <div class="org">"Palmetto Film House (PFH)"<span>Miami, FL</span></div>
  <div class="role">Sound Engineer<br>Edited and mixed recorded field audio to professional standards.<br>Matched audio with motion picture video to create a seamless product.<br>Recorded automated dialogue replacement (ADR) audio and integrated into motion picture video project using TrackLab 11.<br>Recorded foley sound effects to be added to film, video, and other media in post-production.<br>Composed and recorded original music to accompany various video projects.</div>
</article>
<article class="job" style="top:763px">
  <div class="dates">05. 2013 - 10. 2013</div>
  <div class="rule" style="height:122px"></div>
  <div class="org">"Northgate Retail Corporation"<span>Atlanta, GA</span></div>
  <div class="role">Sales Associate<br>Provided customer service, maintained a clean and organized work environment, assisted in sales, and performed cashier responsibilities.</div>
</article>
<article class="job" style="top:896px">
  <div class="dates">06. 2012 - 08. 2012</div>
  <div class="rule" style="height:140px"></div>
  <div class="org">"Georgia CAG"<span>(Civic Action Group)</span><span>Atlanta, GA</span></div>
  <div class="role">On-Site Promoter/Intern<br>Promoted and advertised various campaigns and managed various office tasks, such as setting up site maps and organizing and sorting non-profit donations.</div>
</article>
<article class="job" style="top:1052px">
  <div class="dates">06. 2011 – 08. 2011</div>
  <div class="rule" style="height:122px"></div>
  <div class="org">"Keystone Direct, Incorporated"<span>Atlanta, GA</span></div>
  <div class="role">Product Marketing Consultant<br>Conducted direct sales and marketing of subsidiary product line through establishing a compelling value proposition, overcoming objections, and closing the sale.</div>
</article>

<h2 class="side-head" style="top:231px">PROFILE</h2>
<div class="profile">
  <p>Recent graduate of a highly ranked university seeking opportunities to apply composition and production talents across a variety of music genres and other media. Expertise lies in delivering high quality sound design, editing, mixing, and recording.</p>
  <p>Excellent interpersonal skills and the ability to build strong relationships with people at all levels.&nbsp; Exceptionally motivated self-starter and creative problem solver who enjoys working collaboratively on teams.</p>
</div>

<h2 class="side-head" style="top:510px">QUALIFICATIONS</h2>
<ul class="quals">
  <li>Media Production Software (TrackLab 11)</li>
  <li>Sound Design</li>
  <li>Sound Acoustics</li>
  <li>Studio Recording</li>
  <li>Audio Editing</li>
  <li>Audio Mixing</li>
  <li>Analog/Digital Board Operation</li>
  <li>Music Arranging</li>
  <li>Music Composition</li>
  <li>Music Production</li>
  <li>Composing Sheet Music</li>
  <li>Singer Songwriter</li>
  <li>Rhythm Guitarist</li>
</ul>

<h2 class="side-head" style="top:844px">HONORS/AWARDS</h2>
<ul class="honors">
  <li>Best Film and Score: Frights and Frames<br>2015 Competition (Coral Bay University)</li>
  <li>Everett J Calloway Scholar</li>
  <li>Best New Member,<br>Delta Kappa Sigma Fraternity, Inc.</li>
  <li>Coral Bay University Homecoming King, 2012</li>
</ul>

<h2 class="side-head" style="top:1014px">PROFESSIONAL AFFILIATIONS</h2>
<ul class="affils">
  <li>Member, Guild of Contemporary Composers (GCC)</li>
  <li>Member, National Alliance of Composers, Authors, and Publishers (NACAP)</li>
  <li>Member, Sound Engineering Guild (SEG)</li>
  <li>Member, Delta Kappa Sigma Fraternity, Incorporated</li>
</ul>
</body>
</html>
```